Turn this into a clear and concise

Attached is a screen shot that we currently show to investors from a software program. We need you to illustrate this in a much more professional looking and easy to view and understand way. If we like your style and attention to detail there is more work behind this.
Industry/Entity Type
Software

```html
<!DOCTYPE html>
<html lang="en">
<head>
<meta charset="utf-8">
<title>Intra-Day Countertrend US Hours</title>
<link rel="stylesheet" href="https://fonts.googleapis.com/css2?family=Source+Sans+3:wght@400;600;700&display=swap">
<style>
  :root {
    --page: #ffffff;
    --ink: #111111;
    --frame: #10505f;
    --plot: #2c3445;
    --session: #2a3327;
    --timebar: #1a1e26;
    --grid: #ffffff;
    --grid-dim: #8a93a3;
    --up: #a9d99b;
    --down: #ec1d24;
    --wick: #000000;
    --osc: #5fbf7a;
    --vol: #f08a24;
    --stop: #ef2328;
    --sell: #ef8a2a;
    --trail: #93278f;
    --buy: #3a53a4;
  }
  html, body { margin: 0; padding: 0; overflow: hidden; background: var(--page); }
  .canvas { width: 1200px; height: 857px; display: block; }
  .canvas text { font-family: "Source Sans 3", sans-serif; }
  .title { font-size: 46px; fill: var(--ink); }
  .subtitle { font-size: 29px; fill: var(--ink); }
  .panel-title { font-size: 39px; fill: var(--ink); }
  .axis-label { font-size: 11px; font-weight: 700; fill: #ffffff; }
  .axis-label-sm { font-size: 8px; fill: #ffffff; }
  .time-label { font-size: 10px; fill: #ffffff; }
  .legend-label { font-size: 9px; fill: var(--ink); }
  .candle-up { fill: var(--up); stroke: var(--wick); stroke-width: 1; }
  .candle-down { fill: var(--down); stroke: var(--wick); stroke-width: 1; }
  .wick { stroke: var(--wick); stroke-width: 1.4; }
  .grid-line { stroke: var(--grid); stroke-width: 1; }
  .grid-dot { stroke: var(--grid-dim); stroke-width: 1; stroke-dasharray: 2 2; }
  .tick { stroke: #ffffff; stroke-width: 1; }
  .osc-line { fill: none; stroke: var(--osc); stroke-width: 1.2; }
  .vol-bar { stroke: var(--vol); stroke-width: 2.4; }
</style>
</head>
<body>
<svg class="canvas" viewBox="0 0 1400 1000" width="1200" height="857" xmlns="http://www.w3.org/2000/svg" xmlns:xlink="http://www.w3.org/1999/xlink">
  <defs>
    <g id="chart-base">
      <rect x="0" y="0" width="656" height="513" fill="var(--frame)"/>
      <rect x="0" y="0" width="553" height="456" fill="var(--plot)"/>
      <rect x="129" y="0" width="332" height="261" fill="var(--session)"/>
      <rect x="0" y="456" width="553" height="27" fill="var(--timebar)"/>
      <g class="grid">
        <line class="grid-line" x1="80" y1="0" x2="80" y2="456"/>
        <line class="grid-line" x1="228" y1="0" x2="228" y2="456"/>
        <line class="grid-line" x1="374" y1="0" x2="374" y2="456"/>
        <line class="grid-line" x1="520" y1="0" x2="520" y2="456"/>
        <line class="grid-line" x1="0" y1="105" x2="553" y2="105"/>
        <line class="grid-line" x1="0" y1="175" x2="553" y2="175"/>
        <line class="grid-line" x1="0" y1="229" x2="553" y2="229"/>
        <line class="grid-line" x1="0" y1="263" x2="553" y2="263"/>
        <line class="grid-line" x1="0" y1="351" x2="553" y2="351"/>
        <line class="grid-line" x1="0" y1="369" x2="553" y2="369"/>
        <line class="grid-line" x1="0" y1="404" x2="553" y2="404"/>
        <line class="grid-dot" x1="0" y1="72" x2="553" y2="72"/>
        <line class="grid-dot" x1="0" y1="89" x2="553" y2="89"/>
      </g>
      <g class="ticks">
        <line class="tick" x1="553" y1="16" x2="561" y2="16"/>
        <line class="tick" x1="553" y1="35" x2="558" y2="35"/>
        <line class="tick" x1="553" y1="53" x2="558" y2="53"/>
        <line class="tick" x1="553" y1="72" x2="558" y2="72"/>
        <line class="tick" x1="553" y1="89" x2="558" y2="89"/>
        <line class="tick" x1="553" y1="107" x2="561" y2="107"/>
        <line class="tick" x1="553" y1="124" x2="558" y2="124"/>
        <line class="tick" x1="553" y1="141" x2="558" y2="141"/>
        <line class="tick" x1="553" y1="158" x2="558" y2="158"/>
        <line class="tick" x1="553" y1="175" x2="561" y2="175"/>
        <line class="tick" x1="553" y1="193" x2="558" y2="193"/>
        <line class="tick" x1="553" y1="211" x2="558" y2="211"/>
        <line class="tick" x1="553" y1="229" x2="561" y2="229"/>
        <line class="tick" x1="553" y1="246" x2="558" y2="246"/>
        <line class="tick" x1="553" y1="263" x2="561" y2="263"/>
        <line class="tick" x1="553" y1="281" x2="558" y2="281"/>
        <line class="tick" x1="553" y1="298" x2="558" y2="298"/>
        <line class="tick" x1="553" y1="316" x2="558" y2="316"/>
        <line class="tick" x1="553" y1="334" x2="558" y2="334"/>
        <line class="tick" x1="553" y1="351" x2="561" y2="351"/>
        <line class="tick" x1="553" y1="369" x2="561" y2="369"/>
        <line class="tick" x1="553" y1="387" x2="558" y2="387"/>
        <line class="tick" x1="553" y1="404" x2="561" y2="404"/>
        <line class="tick" x1="553" y1="422" x2="558" y2="422"/>
        <line class="tick" x1="553" y1="439" x2="558" y2="439"/>
      </g>
      <g class="price-axis">
        <text class="axis-label" x="572" y="20">137’24</text>
        <text class="axis-label-sm" x="572" y="38">137’18</text>
        <text class="axis-label-sm" x="572" y="56">137’16</text>
        <text class="axis-label-sm" x="572" y="75">137’14</text>
        <text class="axis-label-sm" x="572" y="92">137’12</text>
        <text class="axis-label" x="572" y="111">137’08</text>
        <text class="axis-label" x="572" y="179">136’28</text>
        <text class="axis-label" x="572" y="233">136’16</text>
        <text class="axis-label" x="572" y="268">100</text>
        <text class="axis-label" x="572" y="355">0</text>
        <text class="axis-label" x="572" y="374">20,000</text>
        <text class="axis-label" x="572" y="408">10,000</text>
      </g>
      <g class="time-axis">
        <text class="time-label" x="80" y="472" text-anchor="middle">8 AM</text>
        <text class="time-label" x="228" y="472" text-anchor="middle">9 AM</text>
        <text class="time-label" x="374" y="472" text-anchor="middle">10 AM</text>
        <text class="time-label" x="520" y="472" text-anchor="middle">11 AM</text>
      </g>
      <line x1="0" y1="281" x2="553" y2="281" stroke="var(--sell)" stroke-width="1.4"/>
      <polyline class="osc-line" points="10,316 22,333 34,336 58,336 70,318 82,319 106,331 118,332 148,347 194,349 206,322 222,321 234,314 246,314 258,301 270,299 282,312 294,313 318,289 330,288 340,270 356,268 370,279 378,299 394,311 406,297 418,301 430,301 468,272 480,293 506,291 528,272 542,271"/>
      <g class="volume">
        <line class="vol-bar" x1="10" y1="456" x2="10" y2="448"/>
        <line class="vol-bar" x1="21" y1="456" x2="21" y2="436"/>
        <line class="vol-bar" x1="33" y1="456" x2="33" y2="443"/>
        <line class="vol-bar" x1="46" y1="456" x2="46" y2="445"/>
        <line class="vol-bar" x1="57" y1="456" x2="57" y2="448"/>
        <line class="vol-bar" x1="68" y1="456" x2="68" y2="446"/>
        <line class="vol-bar" x1="95" y1="456" x2="95" y2="444"/>
        <line class="vol-bar" x1="107" y1="456" x2="107" y2="445"/>
        <line class="vol-bar" x1="119" y1="456" x2="119" y2="444"/>
        <line class="vol-bar" x1="131" y1="456" x2="131" y2="427"/>
        <line class="vol-bar" x1="143" y1="456" x2="143" y2="418"/>
        <line class="vol-bar" x1="155" y1="456" x2="155" y2="431"/>
        <line class="vol-bar" x1="167" y1="456" x2="167" y2="364"/>
        <line class="vol-bar" x1="180" y1="456" x2="180" y2="400"/>
        <line class="vol-bar" x1="191" y1="456" x2="191" y2="378"/>
        <line class="vol-bar" x1="203" y1="456" x2="203" y2="417"/>
        <line class="vol-bar" x1="216" y1="456" x2="216" y2="419"/>
        <line class="vol-bar" x1="229" y1="456" x2="229" y2="442"/>
        <line class="vol-bar" x1="241" y1="456" x2="241" y2="439"/>
        <line class="vol-bar" x1="253" y1="456" x2="253" y2="426"/>
        <line class="vol-bar" x1="265" y1="456" x2="265" y2="429"/>
        <line class="vol-bar" x1="277" y1="456" x2="277" y2="441"/>
        <line class="vol-bar" x1="289" y1="456" x2="289" y2="447"/>
        <line class="vol-bar" x1="301" y1="456" x2="301" y2="444"/>
        <line class="vol-bar" x1="313" y1="456" x2="313" y2="437"/>
        <line class="vol-bar" x1="325" y1="456" x2="325" y2="440"/>
        <line class="vol-bar" x1="338" y1="456" x2="338" y2="405"/>
        <line class="vol-bar" x1="349" y1="456" x2="349" y2="427"/>
        <line class="vol-bar" x1="362" y1="456" x2="362" y2="430"/>
        <line class="vol-bar" x1="374" y1="456" x2="374" y2="443"/>
        <line class="vol-bar" x1="386" y1="456" x2="386" y2="424"/>
        <line class="vol-bar" x1="398" y1="456" x2="398" y2="436"/>
        <line class="vol-bar" x1="410" y1="456" x2="410" y2="436"/>
        <line class="vol-bar" x1="422" y1="456" x2="422" y2="440"/>
        <line class="vol-bar" x1="434" y1="456" x2="434" y2="439"/>
        <line class="vol-bar" x1="447" y1="456" x2="447" y2="435"/>
        <line class="vol-bar" x1="459" y1="456" x2="459" y2="430"/>
        <line class="vol-bar" x1="472" y1="456" x2="472" y2="441"/>
        <line class="vol-bar" x1="484" y1="456" x2="484" y2="436"/>
        <line class="vol-bar" x1="496" y1="456" x2="496" y2="437"/>
        <line class="vol-bar" x1="508" y1="456" x2="508" y2="427"/>
        <line class="vol-bar" x1="519" y1="456" x2="519" y2="430"/>
        <line class="vol-bar" x1="532" y1="456" x2="532" y2="444"/>
      </g>
    </g>

    <g id="candles-core">
      <line class="wick" x1="48" y1="396" x2="48" y2="408"/><rect class="candle-up" x="45" y="398" width="6" height="8"/>
      <line class="wick" x1="60" y1="404" x2="60" y2="428"/><rect class="candle-down" x="57" y="406" width="6" height="16"/>
      <line class="wick" x1="72" y1="422" x2="72" y2="442"/><rect class="candle-down" x="69" y="424" width="6" height="6"/>
      <line class="wick" x1="84" y1="430" x2="92" y2="430"/>
      <line class="wick" x1="96" y1="426" x2="96" y2="436"/><line class="wick" x1="92" y1="430" x2="100" y2="430"/>
      <line class="wick" x1="108" y1="420" x2="108" y2="432"/><rect class="candle-up" x="105" y="424" width="6" height="6"/>
      <line class="wick" x1="120" y1="414" x2="120" y2="426"/><rect class="candle-up" x="117" y="418" width="6" height="4"/>
      <line class="wick" x1="132" y1="420" x2="132" y2="432"/><rect class="candle-down" x="129" y="424" width="6" height="6"/>
      <line class="wick" x1="144" y1="428" x2="144" y2="442"/><line class="wick" x1="140" y1="432" x2="148" y2="432"/>
      <line class="wick" x1="156" y1="428" x2="156" y2="442"/><line class="wick" x1="152" y1="432" x2="160" y2="432"/>
      <line class="wick" x1="168" y1="432" x2="168" y2="450"/><rect class="candle-down" x="165" y="443" width="6" height="5"/>
      <line class="wick" x1="180" y1="446" x2="180" y2="484"/><rect class="candle-down" x="177" y="448" width="6" height="30"/>
      <line class="wick" x1="192" y1="476" x2="192" y2="492"/><rect class="candle-down" x="189" y="478" width="6" height="8"/>
      <line class="wick" x1="204" y1="486" x2="204" y2="558"/><rect class="candle-down" x="201" y="492" width="6" height="36"/>
      <line class="wick" x1="216" y1="532" x2="216" y2="570"/><rect class="candle-down" x="213" y="534" width="6" height="18"/>
      <line class="wick" x1="228" y1="552" x2="228" y2="588"/><line class="wick" x1="224" y1="556" x2="232" y2="556"/>
      <line class="wick" x1="240" y1="526" x2="240" y2="558"/><rect class="candle-up" x="237" y="528" width="6" height="24"/>
      <line class="wick" x1="252" y1="518" x2="252" y2="534"/><rect class="candle-up" x="249" y="522" width="6" height="8"/>
      <line class="wick" x1="264" y1="518" x2="264" y2="534"/><rect class="candle-up" x="261" y="520" width="6" height="8"/>
      <line class="wick" x1="276" y1="516" x2="276" y2="528"/><rect class="candle-up" x="273" y="520" width="6" height="6"/>
      <line class="wick" x1="288" y1="504" x2="288" y2="524"/><rect class="candle-up" x="285" y="510" width="6" height="12"/>
      <line class="wick" x1="300" y1="498" x2="300" y2="512"/><line class="wick" x1="296" y1="504" x2="304" y2="504"/>
      <line class="wick" x1="312" y1="506" x2="312" y2="524"/><rect class="candle-down" x="309" y="510" width="6" height="12"/>
      <line class="wick" x1="324" y1="510" x2="324" y2="528"/><line class="wick" x1="320" y1="516" x2="328" y2="516"/>
      <line class="wick" x1="336" y1="508" x2="336" y2="524"/><line class="wick" x1="332" y1="514" x2="340" y2="514"/>
      <line class="wick" x1="348" y1="498" x2="348" y2="520"/><rect class="candle-up" x="345" y="502" width="6" height="14"/>
      <line class="wick" x1="360" y1="496" x2="360" y2="512"/><rect class="candle-up" x="357" y="502" width="6" height="6"/>
      <line class="wick" x1="370" y1="466" x2="370" y2="520"/><rect class="candle-up" x="367" y="472" width="6" height="32"/>
      <line class="wick" x1="382" y1="462" x2="382" y2="484"/><rect class="candle-up" x="379" y="466" width="6" height="14"/>
      <line class="wick" x1="394" y1="462" x2="394" y2="480"/><rect class="candle-down" x="391" y="466" width="6" height="6"/>
      <line class="wick" x1="406" y1="462" x2="406" y2="494"/><rect class="candle-down" x="403" y="466" width="6" height="24"/>
      <line class="wick" x1="418" y1="484" x2="418" y2="520"/><rect class="candle-down" x="415" y="490" width="6" height="14"/>
      <line class="wick" x1="430" y1="482" x2="430" y2="508"/><rect class="candle-up" x="427" y="484" width="6" height="20"/>
      <line class="wick" x1="442" y1="482" x2="442" y2="500"/><line class="wick" x1="438" y1="490" x2="446" y2="490"/>
      <line class="wick" x1="454" y1="482" x2="454" y2="502"/><line class="wick" x1="450" y1="490" x2="458" y2="490"/>
      <line class="wick" x1="466" y1="474" x2="466" y2="496"/><rect class="candle-up" x="463" y="478" width="6" height="14"/>
      <line class="wick" x1="478" y1="460" x2="478" y2="490"/><rect class="candle-up" x="475" y="466" width="6" height="18"/>
      <line class="wick" x1="490" y1="446" x2="490" y2="468"/><rect class="candle-up" x="487" y="448" width="6" height="18"/>
      <line class="wick" x1="502" y1="446" x2="502" y2="470"/><rect class="candle-down" x="499" y="448" width="6" height="18"/>
      <line class="wick" x1="514" y1="454" x2="514" y2="468"/><rect class="candle-up" x="511" y="458" width="6" height="8"/>
      <line class="wick" x1="526" y1="446" x2="526" y2="468"/><rect class="candle-up" x="523" y="448" width="6" height="18"/>
    </g>
  </defs>

  <text class="title" x="750" y="150" text-anchor="middle">INTRA-DAY COUNTERTREND US HOURS</text>
  <text class="subtitle" x="750" y="202" text-anchor="middle">30 year Treasury Bond, 7/31/14 “Payroll Friday”</text>

  <text class="panel-title" x="357" y="295" text-anchor="middle">Entry (Sell)</text>
  <text class="panel-title" x="1073" y="305" text-anchor="middle">Exit (Buy)</text>

  <g class="chart chart-entry">
    <use xlink:href="#chart-base" x="34" y="329"/>
    <line x1="34" y1="346" x2="587" y2="346" stroke="var(--stop)" stroke-width="1.2"/>
    <line x1="34" y1="364" x2="587" y2="364" stroke="var(--sell)" stroke-width="1.2" stroke-dasharray="2 2"/>
    <line x1="34" y1="382" x2="587" y2="382" stroke="var(--sell)" stroke-width="1.2" stroke-dasharray="2 2"/>
    <use xlink:href="#candles-core"/>
    <line class="wick" x1="538" y1="436" x2="538" y2="464"/><rect class="candle-up" x="535" y="440" width="6" height="20"/>
    <line class="wick" x1="550" y1="418" x2="550" y2="442"/><rect class="candle-up" x="547" y="422" width="6" height="16"/>
    <line class="wick" x1="562" y1="414" x2="562" y2="432"/><line class="wick" x1="558" y1="422" x2="566" y2="422"/>
    <path d="M563 378 h6 v10 h4 l-7 8 l-7 -8 h4 z" fill="var(--stop)"/>
  </g>

  <g class="chart chart-exit">
    <use xlink:href="#chart-base" x="714" y="333"/>
    <line x1="690" y1="438" x2="1267" y2="438" stroke="var(--buy)" stroke-width="1.2"/>
    <line x1="714" y1="368" x2="1267" y2="368" stroke="var(--sell)" stroke-width="1.2" stroke-dasharray="2 2"/>
    <use xlink:href="#candles-core" x="680" y="4"/>
    <line class="wick" x1="1204" y1="436" x2="1204" y2="460"/><rect class="candle-up" x="1201" y="440" width="6" height="16"/>
    <line class="wick" x1="1215" y1="414" x2="1215" y2="438"/><rect class="candle-up" x="1212" y="418" width="6" height="14"/>
    <line class="wick" x1="1226" y1="402" x2="1226" y2="422"/><rect class="candle-up" x="1223" y="406" width="6" height="12"/>
    <line class="wick" x1="1238" y1="396" x2="1238" y2="414"/><rect class="candle-up" x="1235" y="400" width="6" height="12"/>
    <line class="wick" x1="1250" y1="394" x2="1250" y2="408"/><line class="wick" x1="1246" y1="402" x2="1254" y2="402"/>
    <line class="wick" x1="1262" y1="398" x2="1262" y2="412"/><line class="wick" x1="1258" y1="404" x2="1266" y2="404"/>
    <path d="M1230 366 h6 v10 h4 l-7 8 l-7 -8 h4 z" fill="var(--stop)"/>
  </g>

  <g class="legend">
    <rect x="207" y="867" width="82" height="24" fill="var(--stop)"/>
    <text class="legend-label" x="207" y="908">STOP LOSS ORDER</text>
    <rect x="343" y="869" width="82" height="24" fill="var(--sell)"/>
    <text class="legend-label" x="339" y="908">SELL LIMIT ORDER</text>
    <rect x="903" y="866" width="82" height="24" fill="var(--trail)"/>
    <text class="legend-label" x="905" y="910">TRALING STOP ORDER</text>
    <rect x="1035" y="866" width="82" height="24" fill="var(--buy)"/>
    <text class="legend-label" x="1034" y="910">BUY LIMIT ORDER</text>
  </g>
</svg>
</body>
</html>
```